Business Card Design for Lawn Management

Lawn Management

Industry/Entity Type

Business

Contact Information for Business Card

Calloway Lawn Management
Joel Calloway
Calloway_Lawn@brindlemail.com
404-555-0172

```html
<!DOCTYPE html>
<html lang="en">
<head>
<meta charset="utf-8">
<title>Calloway Lawn Management – Business Cards</title>
<link href="https://fonts.googleapis.com/css2?family=Michroma&display=swap" rel="stylesheet">
<style>
  :root {
    --page: #e4e5e6;
    --card: #f7f7f7;
    --green: #2e9a3e;
    --green-light: #4cb556;
    --grey: #a9aaac;
    --grey-light: #d2d3d4;
    --ink: #3a3a3a;
  }
  * { margin: 0; padding: 0; box-sizing: border-box; }
  html, body { width: 1200px; height: 900px; overflow: hidden; background: var(--page); }
  body { position: relative; font-family: "Michroma", sans-serif; }

  .card {
    position: absolute; left: 250px;
    width: 700px; height: 400px;
    background: linear-gradient(160deg, #ffffff 0%, var(--card) 60%, #ececec 100%);
    border-radius: 32px;
    overflow: hidden;
    box-shadow: 0 8px 24px rgba(0,0,0,.12);
  }
  .card-front { top: 30px; }
  .card-back { top: 470px; }
  .swoosh { position: absolute; inset: 0; width: 100%; height: 100%; }

  /* front */
  .brand {
    position: absolute; left: 255px; top: 42px; width: 280px;
    text-align: center; color: var(--green);
  }
  .brand-mark {
    display: block; width: 44px; height: 44px; margin: 0 auto 12px;
    border-radius: 50%; background: var(--green);
  }
  .brand-name { display: block; font-size: 24px; letter-spacing: 1px; line-height: 1.1; }
  .brand-sub { display: block; font-size: 12px; margin-top: 3px; }

  .divider {
    position: absolute; left: 382px; top: 180px;
    width: 2px; height: 104px; background: var(--grey);
  }
  .person {
    position: absolute; right: 332px; top: 186px;
    text-align: right; color: var(--ink); font-size: 12px; line-height: 1.55;
    font-variant: small-caps; white-space: nowrap;
  }
  .person-name { color: var(--green); font-size: 14px; }
  .person-role { margin-bottom: 6px; }

  .contacts {
    position: absolute; left: 398px; top: 184px;
    list-style: none; color: var(--ink); font-size: 12px; line-height: 1.6;
    font-variant: small-caps; white-space: nowrap;
  }
  .contacts li { display: flex; align-items: center; gap: 7px; }
  .contacts li.gap { margin-top: 4px; }
  .icon { width: 13px; height: 13px; flex: none; }

  /* back */
  .back-brand {
    position: absolute; left: 0; right: 0; top: 110px;
    text-align: center; color: var(--green);
  }
  .back-mark {
    display: block; width: 80px; height: 80px; margin: 0 auto 22px;
    border-radius: 50%; background: var(--green);
  }
  .back-name { display: block; font-size: 42px; letter-spacing: 2px; line-height: 1.1; }
  .back-sub { display: block; font-size: 19px; margin-top: 6px; }
</style>
</head>
<body>
  <section class="card card-front" aria-label="Business card, front">
    <svg class="swoosh" viewBox="0 0 1040 594" preserveAspectRatio="none" aria-hidden="true">
      <defs>
        <linearGradient id="greenBand" x1="0" y1="0" x2="1" y2="1">
          <stop offset="0" stop-color="#4cb556"/>
          <stop offset="1" stop-color="#2e9a3e"/>
        </linearGradient>
        <linearGradient id="greyBand" x1="0" y1="0" x2="1" y2="0">
          <stop offset="0" stop-color="#a9aaac"/>
          <stop offset="1" stop-color="#d2d3d4"/>
        </linearGradient>
      </defs>
      <path d="M0 250 C 120 190, 250 150, 360 120 C 250 190, 140 280, 0 400 Z" fill="url(#greyBand)"/>
      <path d="M0 400 C 140 290, 260 200, 360 120 C 290 230, 200 360, 120 440 C 300 520, 520 570, 760 594 L 0 594 Z" fill="url(#greyBand)" opacity=".55"/>
      <path d="M0 330 C 80 300, 150 270, 200 250 C 180 330, 190 410, 260 460 C 400 540, 580 575, 760 594 L 0 594 Z" fill="url(#greenBand)"/>
      <path d="M0 470 C 160 520, 380 560, 620 594 L 0 594 Z" fill="#f2f2f2"/>
      <path d="M0 520 C 200 560, 420 585, 600 594 L 0 594 Z" fill="#c8c9ca"/>
    </svg>

    <div class="brand">
      <span class="brand-mark" aria-hidden="true"></span>
      <span class="brand-name">CALLOWAY</span>
      <span class="brand-sub">Lawn Management</span>
    </div>

    <div class="person">
      <div class="person-name">Joel Calloway</div>
      <div class="person-role">Owner / C.E.O</div>
      <div>Suite # 118, Elm Bldg,</div>
      <div>GA 30317</div>
    </div>

    <div class="divider" aria-hidden="true"></div>

    <ul class="contacts">
      <li>
        <svg class="icon" viewBox="0 0 18 18" aria-hidden="true"><circle cx="9" cy="9" r="9" fill="var(--green)"/><path d="M6 4.5 L8 6.5 L7 8 C7.6 9.4 8.6 10.4 10 11 L11.5 10 L13.5 12 L12 13.5 C8.5 13 5 9.5 4.5 6 Z" fill="#fff"/></svg>
        404-555-0172
      </li>
      <li>
        <svg class="icon" viewBox="0 0 18 18" aria-hidden="true"><circle cx="9" cy="9" r="9" fill="var(--green)"/><rect x="6" y="4" width="6" height="10" rx="1" fill="#fff"/></svg>
        404-555-0186
      </li>
      <li>
        <svg class="icon" viewBox="0 0 18 18" aria-hidden="true"><circle cx="9" cy="9" r="9" fill="var(--green)"/><rect x="4.5" y="7" width="9" height="5" fill="#fff"/><rect x="6" y="4.5" width="6" height="3" fill="#fff"/></svg>
        404-555-0194
      </li>
      <li class="gap">
        <svg class="icon" viewBox="0 0 18 18" aria-hidden="true"><circle cx="9" cy="9" r="9" fill="var(--green)"/><rect x="4.5" y="5.5" width="9" height="7" fill="#fff"/><path d="M4.5 5.5 L9 9.5 L13.5 5.5" fill="none" stroke="var(--green)" stroke-width="1.2"/></svg>
        Calloway_Lawn@brindlemail.com
      </li>
      <li>
        <svg class="icon" viewBox="0 0 18 18" aria-hidden="true"><circle cx="9" cy="9" r="9" fill="var(--green)"/><circle cx="9" cy="9" r="5" fill="none" stroke="#fff" stroke-width="1.2"/><path d="M4 9 H14 M9 4 V14" stroke="#fff" stroke-width="1"/></svg>
        www.callowaylawn.com
      </li>
    </ul>
  </section>

  <section class="card card-back" aria-label="Business card, back">
    <div class="back-brand">
      <span class="back-mark" aria-hidden="true"></span>
      <span class="back-name">CALLOWAY</span>
      <span class="back-sub">Lawn Management</span>
    </div>
  </section>
</body>
</html>
```